43 Year Old Construction firm needs Updated Business Card & Stationery Design

We are an established and well known (in our market) commercial construction firm. We need a cleaner and more modern look for our corporate identity material. We would like to continue to use our current colors and logo.
We are thinking about incorporating a slogan on our business card (either front or back): "Striving to be the most trusted builder in our market." The text could change at some point. Our website is www.kradworth.example . Sample card is attached. Some will have more phone numbers, etc...
Updates

Target Market(s)

Commercial and institutional clients.

Industry/Entity Type

Construction Company

Contact Information for Business Card

See attached for existing card. But don't be constrained.

Requirements
Must have
• Logo, name, title, address, website, email, phone numbers (as few as one, as many as three)
• Slogan on front or back "Striving to be the most trusted builder in our market"
• Use existing logo and colors

```html
<!DOCTYPE html>
<html lang="en">
<head>
<meta charset="utf-8">
<title>Kradworth Constructors – Stationery</title>
<link href="https://fonts.googleapis.com/css2?family=Open+Sans:wght@400;600;700&display=swap" rel="stylesheet">
<style>
  :root {
    --navy: #1f4e8c;
    --navy-deep: #173f74;
    --green: #17a05b;
    --paper: #ffffff;
    --stage: #e6e7e9;
    --ink: #2d3b55;
    --muted: #6b7486;
    --badge-blue: #d9e6f7;
    --badge-header: #4b6fa8;
    --photo-tone: #c9ccd2;
  }
  * { box-sizing: border-box; margin: 0; padding: 0; }
  html, body { width: 1191px; height: 1200px; overflow: hidden; }
  body {
    background: var(--stage);
    font-family: "Open Sans", Arial, sans-serif;
    color: var(--ink);
    position: relative;
  }
  .piece {
    position: absolute;
    background: var(--paper);
    box-shadow: 0 4px 14px rgba(0,0,0,.12);
  }
  .piece-label {
    position: absolute;
    font-size: 15px;
    color: #8a8f98;
    font-weight: 400;
  }

  /* brand name lockup */
  .brand { display: flex; align-items: center; gap: 6px; }
  .brand-square { background: var(--navy); flex: none; }
  .brand-name { color: var(--navy); font-weight: 700; letter-spacing: .2px; }

  /* envelope */
  .envelope { left: 40px; top: 60px; width: 520px; height: 250px; }
  .envelope-flap {
    position: absolute; left: 0; top: 0; right: 0; height: 34px;
    background: linear-gradient(90deg, var(--navy) 0%, var(--navy) 55%, var(--green) 100%);
    display: flex; align-items: center; justify-content: flex-end; padding-right: 24px;
  }
  .envelope-flap .slogan { color: #dfe8f5; font-size: 9px; font-style: normal; }
  .envelope-return { position: absolute; left: 26px; top: 60px; }
  .envelope-return .brand-square { width: 12px; height: 12px; }
  .envelope-return .brand-name { font-size: 13px; }
  .envelope-return address {
    font-style: normal; font-size: 7.5px; line-height: 1.5; color: var(--muted); margin-top: 6px;
  }
  .envelope-return address strong { color: var(--navy); font-weight: 600; }

  /* note card */
  .note-card { left: 620px; top: 60px; width: 330px; height: 235px; }
  .note-card .brand { position: absolute; left: 22px; top: 108px; }
  .note-card .brand-square { width: 10px; height: 10px; }
  .note-card .brand-name { font-size: 12px; }
  .note-card .web { position: absolute; right: 20px; bottom: 14px; font-size: 7.5px; color: var(--muted); }

  /* letterhead */
  .letterhead { left: 520px; top: 345px; width: 600px; height: 830px; }
  .letterhead-topband { position: absolute; left: 0; right: 0; top: 0; height: 9px; background: var(--green); }
  .letterhead .brand { position: absolute; left: 46px; top: 50px; }
  .letterhead .brand-square { width: 16px; height: 16px; }
  .letterhead .brand-name { font-size: 20px; }
  .letterhead-contact {
    position: absolute; right: 46px; top: 42px; font-style: normal;
    font-size: 10.5px; line-height: 1.55; color: var(--muted);
  }
  .letterhead-contact strong { display: block; color: var(--navy); font-weight: 700; font-size: 12px; }
  .contact-line { display: flex; align-items: center; gap: 5px; }
  .contact-line svg { width: 10px; height: 10px; fill: var(--navy); }
  .contact-gap { height: 8px; }
  .letterhead-slogan {
    position: absolute; left: 0; right: 0; bottom: 28px; text-align: center;
    font-size: 10px; color: var(--muted);
  }
  .letterhead-bottomband { position: absolute; left: 0; right: 0; bottom: 0; height: 9px; background: var(--navy); }

  /* ID badge */
  .badge {
    left: 80px; top: 820px; width: 340px; height: 200px; border-radius: 8px; overflow: hidden;
    background: linear-gradient(180deg, #e8effa 0%, var(--badge-blue) 100%);
  }
  .badge-header { height: 34px; background: var(--badge-header); }
  .badge .brand {
    position: absolute; right: 10px; top: 42px; background: var(--paper); padding: 4px 8px;
  }
  .badge .brand-square { width: 10px; height: 10px; }
  .badge .brand-name { font-size: 12px; }
  .badge-photo {
    position: absolute; left: 30px; top: 52px; width: 100px; height: 120px;
    background: linear-gradient(180deg, #e3e5e8 0%, var(--photo-tone) 100%);
  }
  .badge-fields { position: absolute; left: 150px; top: 78px; font-size: 11px; line-height: 1.2; }
  .badge-fields dt { font-size: 6.5px; color: var(--muted); margin-top: 4px; }
  .badge-fields dd { color: var(--ink); font-weight: 600; }
  .badge-footer { position: absolute; left: 0; right: 0; bottom: 0; height: 5px; background: var(--green); }
</style>
</head>
<body>

  <span class="piece-label" style="left:44px; top:32px;">Envelop</span>
  <span class="piece-label" style="left:624px; top:32px;">Note Card</span>

  <section class="piece envelope" aria-label="Envelope">
    <div class="envelope-flap"><span class="slogan">Striving to be the most trusted builder in our market.</span></div>
    <div class="envelope-return">
      <div class="brand"><span class="brand-square"></span><span class="brand-name">Kradworth</span></div>
      <address>
        <strong>Kradworth Constructors Inc.</strong><br>
        4120 Larkspur Avenue<br>
        Fenton, MO 63099-1400<br>
        T 555-201-4820<br>
        F 555-201-4734<br>
        www.kradworth.example
      </address>
    </div>
  </section>

  <section class="piece note-card" aria-label="Note card">
    <div class="brand"><span class="brand-square"></span><span class="brand-name">Kradworth</span></div>
    <span class="web">www.kradworth.example</span>
  </section>

  <section class="piece letterhead" aria-label="Letterhead">
    <div class="letterhead-topband"></div>
    <div class="brand"><span class="brand-square"></span><span class="brand-name">Kradworth</span></div>
    <address class="letterhead-contact">
      <strong>Kradworth Constructors Inc.</strong>
      4120 Larkspur Avenue<br>
      Fenton, MO 63099-1400
      <div class="contact-gap"></div>
      <span class="contact-line">
        <svg viewBox="0 0 10 10"><path d="M2 0.5h2l.8 2.3-1.3.9a5.5 5.5 0 0 0 2.8 2.8l.9-1.3 2.3.8v2a1 1 0 0 1-1 1A8.5 8.5 0 0 1 1 1.5a1 1 0 0 1 1-1z"/></svg>
        555-201-4820
      </span>
      <span class="contact-line">
        <svg viewBox="0 0 10 10"><rect x="1" y="3" width="8" height="5" rx="1"/><rect x="2.5" y="0.5" width="5" height="3"/></svg>
        555-201-4734
      </span>
      <span class="contact-line" style="padding-left:15px;">www.kradworth.example</span>
    </address>
    <p class="letterhead-slogan">Striving to be the most trusted builder in our market.</p>
    <div class="letterhead-bottomband"></div>
  </section>

  <section class="piece badge" aria-label="Staff ID badge">
    <div class="badge-header"></div>
    <div class="brand"><span class="brand-square"></span><span class="brand-name">Kradworth</span></div>
    <div class="badge-photo" role="img" aria-label="Staff portrait photo"></div>
    <dl class="badge-fields">
      <dt>Name</dt><dd>Daniel Avery</dd>
      <dt>Position</dt><dd>Admin Assistant</dd>
      <dt>Gender</dt><dd>Male</dd>
      <dt>Date</dt><dd>1983.01.01</dd>
    </dl>
    <div class="badge-footer"></div>
  </section>

</body>
</html>
```